VANDREL 2020

I have a front picture for the CD; I have all of the info for the back cover; I need someone to put my idea together with the correct specs; I require a very FAST TURN AROUND!!! I need to get this project to the CD replicator by next week ASAP...

```html
<!DOCTYPE html>
<html lang="en">
<head>
<meta charset="utf-8">
<title>VANDREL 2020 – CD Cover</title>
<link href="https://fonts.googleapis.com/css2?family=Roboto:wght@700;900&family=Teko:wght@500&display=swap" rel="stylesheet">
<style>
  :root {
    --stage: #e4e4e4;
    --flag-red: #c8202b;
    --flag-white: #f1ece6;
    --flag-blue: #233a8c;
    --suit-navy: #1c2238;
    --back-red: #b9242b;
    --back-red-deep: #8f1b20;
    --ink-white: #ffffff;
  }
  * { margin: 0; padding: 0; box-sizing: border-box; }
  html, body { width: 1200px; height: 900px; overflow: hidden; background: var(--stage); }
  .canvas { position: relative; width: 1200px; height: 900px; }

  /* Front cover */
  .front-cover {
    position: absolute; left: 60px; top: 215px; width: 470px; height: 470px;
    overflow: hidden; box-shadow: 0 10px 30px rgba(0,0,0,.18);
  }
  .front-flag {
    position: absolute; inset: 0;
    background:
      linear-gradient(160deg, var(--flag-blue) 0%, var(--flag-blue) 28%, transparent 28.5%),
      linear-gradient(160deg, var(--flag-red) 0%, var(--flag-white) 45%, var(--flag-red) 70%, var(--flag-white) 100%);
  }
  .front-figure {
    position: absolute; left: 110px; top: 250px; width: 280px; height: 220px;
    background: linear-gradient(180deg, #2a3150 0%, var(--suit-navy) 100%);
    border-radius: 60px 60px 0 0;
  }
  .front-title {
    position: absolute; left: 0; right: 0; top: 18px; text-align: center;
    font-family: "Roboto", sans-serif; font-weight: 900; color: var(--ink-white);
    line-height: .86; text-shadow: 0 3px 6px rgba(0,0,0,.25);
  }
  .front-title .title-name { display: block; font-size: 90px; letter-spacing: -4px; }
  .front-title .title-year { display: block; font-size: 118px; letter-spacing: -5px; }
  .front-artist {
    position: absolute; left: 130px; bottom: 30px;
    font-family: "Roboto", sans-serif; font-weight: 700; font-size: 32px;
    color: var(--ink-white); letter-spacing: -1px; transform: rotate(-6deg);
    text-shadow: 0 2px 4px rgba(0,0,0,.35);
  }

  /* Back cover */
  .back-cover {
    position: absolute; left: 570px; top: 215px; width: 580px; height: 470px;
    overflow: hidden; box-shadow: 0 10px 30px rgba(0,0,0,.18);
  }
  .back-crowd {
    position: absolute; inset: 0;
    background: radial-gradient(ellipse at 50% 60%, var(--back-red) 0%, var(--back-red-deep) 100%);
  }
  .back-flag {
    position: absolute; left: 142px; top: 0; width: 290px; height: 125px;
    background: linear-gradient(165deg, var(--flag-blue) 0%, #6d5b8a 28%, var(--flag-red) 48%, var(--flag-white) 70%, var(--flag-red) 100%);
    border-radius: 0 0 6px 10px;
    transform: rotate(2deg);
    transform-origin: left top;
  }
  .back-title {
    position: absolute; left: 0; right: 0; top: 22px; text-align: center;
    font-family: "Roboto", sans-serif; font-weight: 900; color: var(--ink-white);
    line-height: .85; text-shadow: 0 2px 4px rgba(0,0,0,.3);
  }
  .back-title .title-name { display: block; font-size: 46px; letter-spacing: -2px; }
  .back-title .title-year { display: block; font-size: 52px; letter-spacing: -2px; }
  .back-artist {
    position: absolute; left: 0; right: 0; top: 136px; text-align: center;
    font-family: "Roboto", sans-serif; font-weight: 700; font-size: 26px;
    color: var(--ink-white); letter-spacing: -1px;
  }
  .track-list {
    position: absolute; left: 0; right: 0; top: 188px; list-style: none; text-align: center;
    font-family: "Teko", sans-serif; font-weight: 500; font-size: 25px; line-height: 30px;
    color: var(--ink-white); letter-spacing: .5px;
  }
</style>
</head>
<body>
<div class="canvas">

  <section class="front-cover">
    <div class="front-flag" role="img" aria-label="Waving stars and stripes flag photograph"></div>
    <div class="front-figure" role="img" aria-label="Photograph of a man in a navy suit and red tie, arms open"></div>
    <h1 class="front-title">
      <span class="title-name">VANDREL</span>
      <span class="title-year">2020</span>
    </h1>
    <p class="front-artist">Leo Marchetti</p>
  </section>

  <section class="back-cover">
    <div class="back-crowd" role="img" aria-label="Red-tinted photograph of a rally crowd holding signs"></div>
    <div class="back-flag" role="img" aria-label="Photograph of a waving stars and stripes flag"></div>
    <h2 class="back-title">
      <span class="title-name">VANDREL</span>
      <span class="title-year">2020</span>
    </h2>
    <p class="back-artist">Leo Marchetti</p>
    <ol class="track-list">
      <li>1. VANDREL DERANGEMENT SYNDROME</li>
      <li>2. WOW THING</li>
      <li>3. STAR SPANGLED BANNER</li>
      <li>4. AMERICA IS BEAUTIFUL</li>
      <li>5. LET VANDREL BE VANDREL</li>
      <li>6. I BELIEVE IN HIM</li>
      <li>7. HE'S SO BAD</li>
      <li>8. NEVER VANDREL BLUES</li>
      <li>9. PALM HARBOR</li>
    </ol>
  </section>

</div>
</body>
</html>
```